Professional Business Cards for Janitorial Company

We are a Janitorial Company that services Commercial Buildings.

Our Logo is included. It can't look silly or cartoonish. Has to look professional.

Information:
Derek Malloy
Operations Manager
619.437.2086
DMalloy@BrightwayFacilityCare.com
www.BrightwayFacilityCare.com

```html
<!DOCTYPE html>
<html lang="en">
<head>
<meta charset="UTF-8">
<title>Brightway Facility Care – Business Card</title>
<link href="https://fonts.googleapis.com/css2?family=Open+Sans:wght@400;600;700&display=swap" rel="stylesheet">
<style>
  :root {
    --bg: #e9e7e3;
    --brand-blue: #2bb7e4;
    --brand-blue-deep: #1fa6d6;
    --card-white: #ffffff;
    --swoosh-grey: #4a4a4c;
    --shadow: rgba(0, 0, 0, 0.22);
  }
  * { box-sizing: border-box; margin: 0; padding: 0; }
  html, body {
    width: 1200px; height: 803px; overflow: hidden;
    background: var(--bg);
    font-family: "Open Sans", Arial, sans-serif;
  }
  .canvas {
    position: relative; width: 1200px; height: 803px;
  }
  .card {
    position: absolute; top: 252px;
    width: 525px; height: 300px;
    border-radius: 22px; overflow: hidden;
    box-shadow: 0 10px 24px var(--shadow);
  }
  /* Front */
  .card--front {
    left: 50px;
    background: linear-gradient(135deg, var(--brand-blue) 0%, var(--brand-blue-deep) 100%);
    color: var(--card-white);
  }
  .front__bar-left {
    position: absolute; left: 0; top: 128px;
    width: 120px; height: 11px; background: var(--card-white);
  }
  .front__bar-right {
    position: absolute; right: 0; bottom: 34px;
    width: 170px; height: 12px; background: var(--card-white);
  }
  .front__logo {
    position: absolute; left: 150px; top: 70px;
    display: flex; align-items: center; gap: 14px;
  }
  .logo-square {
    width: 46px; height: 46px; border: 5px solid currentColor; border-radius: 4px;
  }
  .logo-name {
    font-weight: 700; font-size: 24px; line-height: 1.05; letter-spacing: 0.2px;
  }
  .front__rule {
    position: absolute; left: 132px; top: 150px;
    width: 290px; height: 5px; background: var(--card-white);
  }
  .front__web {
    position: absolute; left: 132px; top: 166px;
    font-size: 14px; font-weight: 600;
  }
  /* Back */
  .card--back {
    left: 625px;
    background: var(--card-white);
  }
  .back__shapes { position: absolute; inset: 0; }
  .back__logo {
    position: absolute; right: 40px; top: 62px;
    display: flex; align-items: center; gap: 12px;
    color: var(--brand-blue);
  }
  .back__logo .logo-square { width: 40px; height: 40px; border-width: 5px; }
  .back__logo .logo-name { font-size: 21px; }
  .back__rule {
    position: absolute; right: 30px; top: 124px;
    width: 230px; height: 4px; background: var(--brand-blue);
  }
  .contact {
    position: absolute; left: 34px; top: 150px;
    color: var(--card-white);
  }
  .contact__name { font-size: 17px; font-weight: 700; }
  .contact__title { font-size: 11px; margin-bottom: 8px; }
  .contact__list { list-style: none; }
  .contact__list li {
    display: flex; align-items: center; gap: 8px;
    font-size: 12px; line-height: 18px;
  }
  .contact__list li.no-icon { padding-left: 18px; }
  .icon { width: 10px; height: 10px; flex: none; }
</style>
</head>
<body>
<main class="canvas">

  <section class="card card--front" aria-label="Card front">
    <div class="front__bar-left"></div>
    <div class="front__logo">
      <span class="logo-square"></span>
      <span class="logo-name">Brightway<br>Facility Care</span>
    </div>
    <div class="front__rule"></div>
    <p class="front__web">www.BrightwayFacilityCare.com</p>
    <div class="front__bar-right"></div>
  </section>

  <section class="card card--back" aria-label="Card back">
    <svg class="back__shapes" viewBox="0 0 525 300" width="525" height="300" aria-hidden="true">
      <path d="M0,92 C175,30 335,92 372,300 L350,300 C318,112 165,58 0,112 Z" fill="var(--swoosh-grey)"/>
      <path d="M0,122 C160,70 305,122 338,300 L0,300 Z" fill="var(--brand-blue)"/>
    </svg>

    <div class="back__logo">
      <span class="logo-square"></span>
      <span class="logo-name">Brightway<br>Facility Care</span>
    </div>
    <div class="back__rule"></div>

    <div class="contact">
      <p class="contact__name">Derek Malloy</p>
      <p class="contact__title">Operations Manager</p>
      <ul class="contact__list">
        <li>
          <svg class="icon" viewBox="0 0 10 10"><path d="M2,0.5 L3.6,2.6 L2.7,3.6 C3.3,5 4.9,6.6 6.4,7.3 L7.4,6.4 L9.5,8 L8.3,9.5 C4.5,9 1,5.5 0.5,1.7 Z" fill="#fff"/></svg>
          619.437.2086
        </li>
        <li>
          <svg class="icon" viewBox="0 0 10 10"><rect x="0.5" y="1.5" width="9" height="7" fill="none" stroke="#fff"/><path d="M0.5,1.5 L5,5.5 L9.5,1.5" fill="none" stroke="#fff"/></svg>
          DMalloy@BrightwayFacilityCare.com
        </li>
        <li>
          <svg class="icon" viewBox="0 0 10 10"><circle cx="5" cy="5" r="4.5" fill="none" stroke="#fff"/><ellipse cx="5" cy="5" rx="2" ry="4.5" fill="none" stroke="#fff"/><path d="M0.5,5 H9.5" stroke="#fff"/></svg>
          www.BrightwayFacilityCare.com
        </li>
      </ul>
    </div>
  </section>

</main>
</body>
</html>
```